Business Card Design Competition

We need a business card design for our Internet Marketing company. We require both front and back designs and the final card must be 89x53mm in size, plus crop marks to 91x55mm. Colours as per logo, plus perhaps black and/or grey (#828282).
Final text must be editable (if you can supply an editable Fireworks PNG, even better)...
FRONT TEXT:
Full Name
Position
Address Line
Suburb, State, Postcode
Phone: 0000 000 000
Mobile: 0000 000 000
Email: xxx@brimleafpromo.com.au
Web: www.brimleafpromo.com.au
Rear of card should be a fresh design plus our slogan text: "Getting You Noticed" in large font, then in small text "Brimleaf Holdings Pty Ltd (ABN: 42 563 701 384)".
Target Market(s)
Small/Medium Businesses
Industry/Entity Type
Business
Look and feel
Each slider illustrates characteristics of the customer's brand and the style your logo design should communicate.

```html
<!DOCTYPE html>
<html lang="en">
<head>
<meta charset="utf-8">
<title>Brimleaf Promo – Business Card</title>
<link href="https://fonts.googleapis.com/css2?family=PT+Sans:wght@400;700&display=swap" rel="stylesheet">
<style>
  :root {
    --card-black: #000000;
    --panel-white: #ffffff;
    --ink: #111111;
    --brand-orange: #f39c1f;
    --icon-grey: #828282;
    --page: #ffffff;
  }
  html, body {
    margin: 0;
    padding: 0;
    width: 1200px;
    height: 902px;
    overflow: hidden;
    background: var(--page);
    font-family: "PT Sans", "Myriad Pro", sans-serif;
  }
  .canvas { position: relative; width: 1200px; height: 902px; }
  .shapes { position: absolute; inset: 0; }
  .text { position: absolute; margin: 0; white-space: nowrap; line-height: 1; }

  .slogan { left: 664px; top: 90px; width: 209px; height: 51px;
    display: flex; align-items: center; justify-content: center;
    font-size: 21px; color: var(--ink); }
  .people-icon { position: absolute; left: 744px; top: 162px; width: 100px; height: 88px;
    border-radius: 40px 40px 18px 18px;
    background: linear-gradient(180deg, #8a8a8a, #5e5e5e);
    box-shadow: 0 0 0 5px #f2f2f2; }
  .company { right: 319px; text-align: right; font-size: 17px; color: var(--panel-white); }

  .brand { position: absolute; display: flex; align-items: center; gap: 10px; }
  .brand-dot { border-radius: 50%; background: var(--brand-orange); flex: none; }
  .brand-name { display: block; color: var(--brand-orange); font-weight: 400; line-height: 0.95; white-space: nowrap; }

  .brand--front { left: 322px; top: 203px; }
  .brand--front .brand-dot { width: 96px; height: 96px; }
  .brand--front .brand-name { font-size: 38px; }
  .brand--back { left: 626px; top: 505px; }
  .brand--back .brand-dot { width: 80px; height: 80px; }
  .brand--back .brand-name { font-size: 32px; }

  .holder-name { right: 710px; top: 522px; font-size: 31px; color: var(--panel-white); }
  .holder-role { right: 710px; top: 561px; font-size: 15px; color: var(--panel-white); }
  .mobile-number { left: 381px; top: 601px; font-size: 18px; color: var(--panel-white); }

  .address { left: 581px; top: 614px; font-size: 17.5px; line-height: 21px; color: var(--ink); white-space: normal; }
  .contact { left: 616px; font-size: 18px; color: var(--ink); }
</style>
</head>
<body>
<div class="canvas">
  <svg class="shapes" width="1200" height="902" viewBox="0 0 1200 902">
    <!-- rear side -->
    <rect x="281" y="64" width="621" height="370" fill="var(--card-black)"/>
    <path d="M295,85 H598 Q652,85 652,249 Q652,413 598,413 H295 Z" fill="var(--panel-white)"/>
    <rect x="664" y="90" width="209" height="51" rx="8" fill="var(--panel-white)"/>
    <path d="M829,139 L820,162 L846,139 Z" fill="var(--panel-white)"/>

    <!-- front side -->
    <rect x="281" y="472" width="621" height="370" fill="var(--card-black)"/>
    <path d="M883,494 V820 H580 Q525,820 525,657 Q525,494 580,494 Z" fill="var(--panel-white)"/>

    <!-- mobile icon -->
    <rect x="341" y="598" width="25" height="25" rx="4" fill="none" stroke="var(--panel-white)" stroke-width="1.5"/>
    <rect x="349" y="602" width="9" height="17" rx="1.5" fill="var(--panel-white)"/>
    <rect x="351" y="605" width="5" height="4" fill="var(--card-black)"/>

    <!-- phone icon -->
    <rect x="581" y="695" width="22" height="22" rx="4" fill="none" stroke="var(--ink)" stroke-width="1.5"/>
    <path d="M586,700 q1,-1 3,0 l2,3 q0,1 -1,2 q1,3 4,5 q1,-1 2,-1 l3,2 q1,2 0,3 q-2,2 -4,1 q-7,-3 -10,-10 q-1,-3 1,-5 Z" fill="var(--ink)"/>
    <!-- mail icon -->
    <rect x="581" y="730" width="22" height="22" rx="4" fill="none" stroke="var(--ink)" stroke-width="1.5"/>
    <rect x="585" y="736" width="14" height="10" fill="none" stroke="var(--ink)" stroke-width="1.3"/>
    <path d="M585,736 L592,742 L599,736" fill="none" stroke="var(--ink)" stroke-width="1.3"/>
    <!-- web icon -->
    <rect x="581" y="762" width="22" height="22" rx="4" fill="none" stroke="var(--ink)" stroke-width="1.5"/>
    <rect x="585" y="767" width="14" height="11" rx="1" fill="var(--ink)"/>
    <rect x="587" y="769" width="10" height="7" fill="var(--panel-white)"/>
  </svg>

  <!-- rear side content -->
  <div class="brand brand--front">
    <span class="brand-dot"></span>
    <span class="brand-name">Brimleaf<br>Promo</span>
  </div>
  <p class="text slogan">Getting You Noticed</p>
  <div class="people-icon" role="img" aria-label="Grey icon of two people"></div>
  <p class="text company" style="top:373px;">Brimleaf Holdings Pty Ltd</p>
  <p class="text company" style="top:398px;">(ABN: 42 563 701 384)</p>

  <!-- front side content -->
  <p class="text holder-name">Jordan Ellis</p>
  <p class="text holder-role">Marketing Manager</p>
  <p class="text mobile-number">0000 000 000</p>

  <div class="brand brand--back">
    <span class="brand-dot"></span>
    <span class="brand-name">Brimleaf<br>Promo</span>
  </div>
  <p class="text address">Address Line<br>Suburb, State, Postcode</p>
  <p class="text contact" style="top:698px;">0000 000 000</p>
  <p class="text contact" style="top:732px;">xxx@brimleafpromo.com.au</p>
  <p class="text contact" style="top:763px;">www.brimleafpromo.com.au</p>
</div>
</body>
</html>
```